TAVRO Kiosk Webpage Design

Just need a simple, single page web design. I have a preliminary idea of what I need, just want to add a professional touch to it. We already have the google map locator plug-in. Generic website is already up and I can send the locator plugin when project is complete for final HTML/CSS Coding. Needs to be coded as a responsive design on a flexible grid (i.e. will auto adjust screen for desktop/tablet/mobile devices)
Target Market(s)
Business/Student/General Public, Mobile Office Kiosk Rental Station (Technology-Printing-Scanning-Faxing, etc...)
Industry/Entity Type
It Professional
Coding
Coded - Design and coding required
Number of Pages Required
1 page
Look and feel
Each slider illustrates characteristics of the customer's brand and the style your logo design should communicate.

```html
<!DOCTYPE html>
<html lang="en">
<head>
<meta charset="utf-8">
<title>TAVRO – Mobile Office. Simplified.</title>
<link rel="stylesheet" href="https://fonts.googleapis.com/css2?family=Lato:ital,wght@0,400;0,700;1,400&family=Raleway:wght@400;500&display=swap">
<style>
:root{
  --brand-blue:#145f9b;
  --brand-navy:#0d5a96;
  --sky:#1ba3dc;
  --button:#10a2e0;
  --ink:#333;
  --muted:#666;
  --card:#f1f1f1;
  --rule:#e4e4e4;
  --map:#e8e3d3;
  --white:#fff;
}
*{box-sizing:border-box;margin:0;padding:0}
html,body{width:920px;height:1200px;overflow:hidden;background:var(--white)}
body{position:relative;font-family:'Lato',sans-serif;color:var(--ink)}
.abs{position:absolute}

.site-header{left:0;top:0;width:920px;height:67px;border-top:3px solid var(--sky);background:var(--white);z-index:2}
.social{left:102px;top:24px;display:flex;gap:5px}
.social span{width:20px;height:20px;border-radius:50%;background:var(--brand-blue)}
.social span:nth-child(2){background:var(--sky)}
.social span:nth-child(3){background:#1878b8}
.logo-tab{left:384px;top:60px;width:168px;height:38px;background:var(--white);border-radius:0 0 26px 26px;z-index:2}
.brand{left:384px;top:44px;width:168px;text-align:center;font-weight:700;font-size:24px;color:var(--brand-blue);letter-spacing:1px;z-index:3}
.tagline{right:101px;top:28px;font-weight:700;font-size:16px;color:var(--sky)}

.hero{left:0;top:67px;width:920px;height:252px;background:linear-gradient(100deg,#f4f4f4 0%,#e8e8e8 35%,#cfcfcf 60%,#ebebeb 75%,#bdbdbd 100%)}
.hero-title{left:118px;top:104px;font-weight:700;font-size:20px;line-height:26px;color:var(--brand-blue)}
.hero-arrow{top:170px;width:26px;height:46px;background:rgba(255,255,255,.85)}
.hero-arrow.prev{left:74px;border-radius:0 23px 23px 0}
.hero-arrow.next{left:822px;border-radius:23px 0 0 23px}
.hero-arrow svg{position:absolute;top:15px;left:6px}

.section-title{left:0;width:920px;text-align:center;font-family:'Raleway',sans-serif;font-size:22px;color:var(--brand-blue)}
.divider{left:203px;width:514px;height:14px}
.divider::before{content:"";position:absolute;left:0;right:0;top:6px;height:2px;background:var(--rule)}
.divider::after{content:"";position:absolute;left:250px;top:0;width:14px;height:14px;border-radius:50%;background:var(--brand-blue);box-shadow:0 0 0 4px var(--white)}

.service{top:436px;width:122px;height:103px;background:var(--card);text-align:center}
.service .icon{position:absolute;left:36px;top:-27px;width:50px;height:50px;border-radius:50%;background:radial-gradient(circle at 50% 35%,#1e8fd0,#0c5c98);border:2px solid var(--white)}
.service .icon svg{position:absolute;left:11px;top:11px}
.service h3{margin-top:42px;font-size:15px;font-weight:700;color:#222}
.service p{margin-top:2px;font-size:11px;line-height:14px;color:var(--muted)}

.locator-band{left:0;top:575px;width:920px;height:43px;background:var(--brand-navy);color:var(--white);text-align:center;font-family:'Raleway',sans-serif;font-size:21px;line-height:43px}
.map{left:0;top:618px;width:920px;height:370px;background:linear-gradient(135deg,#ece7d8 0%,#e6e0cf 50%,#dfe5e6 100%)}
.filter-panel{left:100px;top:640px;width:181px;height:156px;background:var(--white);box-shadow:0 1px 4px rgba(0,0,0,.25);padding:14px 16px;font-size:10px;color:var(--muted)}
.filter-panel .count{display:flex;justify-content:space-between}
.filter-panel a{color:#1a5e96;text-decoration:none}
.filter-panel .row{display:flex;justify-content:space-between;border-top:1px solid #ccc;padding:8px 0 8px}
.filter-panel .chev{color:#e2511b;font-size:10px}
.select-btn{position:absolute;right:16px;bottom:16px;width:79px;height:28px;background:var(--button);color:var(--white);border-radius:3px;font-weight:700;font-size:10px;text-align:center;line-height:28px;border-bottom:2px solid #0b7ab0}
.search-panel{left:296px;top:640px;width:523px;height:90px;background:var(--white);box-shadow:0 1px 4px rgba(0,0,0,.25)}
.search-input{position:absolute;left:14px;top:14px;width:454px;height:30px;border:1px solid #bbb;font-style:italic;font-size:10px;color:#777;padding:0 13px;line-height:28px}
.search-input svg{position:absolute;right:8px;top:6px}
.locate-btn{position:absolute;left:484px;top:17px}
.notice{position:absolute;left:0;bottom:0;width:523px;height:33px;background:#222;color:var(--white);font-size:10px;line-height:33px;text-align:center}
.notice .close{position:absolute;right:24px;top:0;font-weight:700;font-size:12px}

.about{left:100px;top:1077px;width:720px;text-align:center;font-size:10px;line-height:17px;color:var(--ink)}
.site-footer{left:0;top:1164px;width:920px;height:36px;background:var(--brand-navy);color:var(--white);text-align:center;font-size:10px;line-height:36px}
</style>
</head>
<body>

<header class="site-header abs">
  <div class="social abs" aria-label="Social links"><span></span><span></span><span></span></div>
  <div class="tagline abs">Mobile Office. Simplified.</div>
</header>
<div class="logo-tab abs"></div>
<div class="brand abs">TAVRO</div>

<section class="hero abs" role="img" aria-label="Abstract grey 3D geometric banner image">
</section>
<h1 class="hero-title abs">LOREM IPSUM DOLOR SIT<br>AMET CONSECTETUER</h1>
<div class="hero-arrow prev abs"><svg width="12" height="16" viewBox="0 0 12 16"><path d="M9 2 3 8l6 6" fill="none" stroke="#333" stroke-width="3"/></svg></div>
<div class="hero-arrow next abs"><svg width="12" height="16" viewBox="0 0 12 16"><path d="M4 2l6 6-6 6" fill="none" stroke="#333" stroke-width="3"/></svg></div>

<h2 class="section-title abs" style="top:349px">OUR SERVICES</h2>
<div class="divider abs" style="top:380px"></div>

<div class="service abs" style="left:102px">
  <div class="icon"><svg width="24" height="24" viewBox="0 0 24 24" fill="none" stroke="#fff" stroke-width="1.6"><rect x="3" y="4" width="18" height="16" rx="1"/><path d="M3 8h18M7 11h5v5H7zM14 12h4M14 15h4"/></svg></div>
  <h3>SURF</h3><p>Lorem ipsum dolor sit<br>amet, consectetu</p>
</div>
<div class="service abs" style="left:251px">
  <div class="icon"><svg width="24" height="24" viewBox="0 0 24 24" fill="none" stroke="#fff" stroke-width="1.6"><rect x="7" y="3" width="10" height="6"/><rect x="3" y="9" width="18" height="8" rx="1"/><rect x="7" y="14" width="10" height="7"/><path d="M9 17h6M9 19h6"/></svg></div>
  <h3>PRINT</h3><p>Lorem ipsum dolor sit<br>amet, consectetu</p>
</div>
<div class="service abs" style="left:399px">
  <div class="icon"><svg width="24" height="24" viewBox="0 0 24 24" fill="none" stroke="#fff" stroke-width="1.6"><path d="M3 7V3h4M17 3h4v4M21 17v4h-4M7 21H3v-4"/><circle cx="12" cy="12" r="5"/><circle cx="12" cy="12" r="2.5"/></svg></div>
  <h3>SCAN</h3><p>Lorem ipsum dolor sit<br>amet, consectetu</p>
</div>
<div class="service abs" style="left:548px">
  <div class="icon"><svg width="24" height="24" viewBox="0 0 24 24" fill="none" stroke="#fff" stroke-width="1.6"><rect x="7" y="3" width="12" height="16" rx="1"/><path d="M5 6v15h11M10 8h6M10 11h6M10 14h6"/></svg></div>
  <h3>COPY</h3><p>Lorem ipsum dolor sit<br>amet, consectetu</p>
</div>
<div class="service abs" style="left:697px">
  <div class="icon"><svg width="24" height="24" viewBox="0 0 24 24" fill="#fff"><rect x="6" y="2" width="12" height="5"/><rect x="2" y="8" width="20" height="10" rx="2"/><rect x="6" y="13" width="12" height="9" fill="#0c5c98" stroke="#fff" stroke-width="1.5"/><path d="M8 16h8M8 19h8" stroke="#fff" stroke-width="1.2"/></svg></div>
  <h3>FAX</h3><p>Lorem ipsum dolor sit<br>amet, consectetu</p>
</div>

<h2 class="locator-band abs">LOCATE YOUR NEAREST TAVRO KIOSK BELOW</h2>
<div class="map abs" role="img" aria-label="Street map of the kiosk locator area"></div>

<div class="filter-panel abs">
  <div class="count"><span>0 of 0 outlets</span><a>Clear All</a></div>
  <a style="display:block;margin:2px 0 10px">Show All</a>
  <div class="row"><span>By Region</span><span class="chev">&#9013;</span></div>
  <div class="row" style="border-top:1px solid #ddd"><span>Category</span><span class="chev">&#9013;</span></div>
  <div class="select-btn">SELECT</div>
</div>

<div class="search-panel abs">
  <div class="search-input">Search For Nearby Stores
    <svg width="16" height="16" viewBox="0 0 16 16" fill="none" stroke="#222" stroke-width="1.6"><circle cx="6.5" cy="6.5" r="5"/><path d="M10 10l5 5"/></svg>
  </div>
  <svg class="locate-btn" width="24" height="24" viewBox="0 0 24 24" fill="none" stroke="#1a6aa5" stroke-width="2"><circle cx="12" cy="12" r="7"/><circle cx="12" cy="12" r="2" fill="#1a6aa5"/><path d="M12 1v6M12 17v6M1 12h6M17 12h6"/></svg>
  <div class="notice">No near by were found. Why not using our search funcation above ?<span class="close">X</span></div>
</div>

<h2 class="section-title abs" style="top:1018px">THE TAVRO KIOSK EXPERIENCE</h2>
<div class="divider abs" style="top:1050px"></div>
<p class="about abs">Lorem ipsum dolor sit amet, consectetuer adipiscing elit, sed diam nonummy nibh euism od tincidunt ut laoreet dolore magna aliquam erat volutpat. Ut wisi enim ad minim venia m, quis nostrud exerci in amet ullamcorper suscipit lobortis nisl ut aliquip ex ea comsed diam nonummy nibh euism od tincidunt uopre laoreet dolore magna aliquam erat volutpat.</p>

<footer class="site-footer abs">© 2015 TAVRO &nbsp;|&nbsp; All Rights Reserved</footer>

</body>
</html>
```